Kestrel Roofing & Restoration Business Card Design

Lookiing for a double sided business card design that will have rounded corners, will look good with Spot UV, Soft Laminate, or Gloss
Front of card should have Logo, Name and Contact Info, License numbers
Back of card should have Logo, maybe other small details

```html
<!DOCTYPE html>
<html lang="en">
<head>
<meta charset="utf-8">
<title>Kestrel Roofing &amp; Restoration – Business Card</title>
<link rel="stylesheet" href="https://fonts.googleapis.com/css2?family=Fredoka:wght@600&family=Inter:wght@400&family=Montserrat:wght@600&family=Space+Mono:ital,wght@1,700&display=swap">
<style>
  :root {
    --backdrop: #474f61;
    --card-base: #567bc1;
    --card-light: #7694cb;
    --deep-blue: #3a4bb8;
    --soft-blue: #7594cc;
    --rule: #ffffff;
    --ink: #ffffff;
  }
  * { box-sizing: border-box; margin: 0; padding: 0; }
  html, body { width: 1200px; height: 800px; overflow: hidden; }
  body { background: var(--backdrop); position: relative; }

  .card {
    position: absolute;
    left: 360px;
    width: 480px;
    height: 275px;
    background: var(--card-base);
    overflow: hidden;
  }
  .card--back { top: 92px; }
  .card--front { top: 434px; }

  .block { position: absolute; }
  .rule { position: absolute; background: var(--rule); }
  .rule--v { width: 1.5px; }
  .rule--h { height: 1.5px; }

  /* back */
  .back__fade-column {
    left: 0; top: 0; width: 77px; height: 203px;
    background: linear-gradient(180deg, var(--deep-blue), var(--soft-blue));
  }
  .back__fade-band {
    left: 232px; top: 0; width: 248px; height: 73px;
    background: linear-gradient(90deg, var(--soft-blue), var(--deep-blue));
  }
  .brand {
    position: absolute;
    font-family: "Montserrat", sans-serif;
    font-weight: 600;
    color: var(--ink);
    line-height: 1.15;
    white-space: nowrap;
  }
  .back__brand {
    left: 253px; top: 140px;
    font-size: 17px;
  }
  .back__brand .brand__name { font-size: 30px; line-height: 1; margin-bottom: 6px; }

  /* front */
  .front__top-band {
    left: 0; top: 0; width: 310px; height: 73px;
    background: var(--card-light);
  }
  .front__corner {
    left: 310px; top: 162px; width: 170px; height: 113px;
    background: var(--card-light);
  }
  .front__brand {
    left: 310px; top: 42px; width: 170px;
    text-align: center;
    font-size: 16px;
  }
  .front__brand .brand__name { font-size: 30px; line-height: 1; }
  .front__brand .brand__divider {
    width: 74px; height: 1.5px; background: var(--deep-blue);
    margin: 14px auto 10px;
  }

  .contact { position: absolute; left: 26px; color: var(--ink); white-space: nowrap; }
  .contact__name {
    top: 116px;
    font-family: "Fredoka", sans-serif;
    font-weight: 600;
    font-size: 28px;
    letter-spacing: -0.3px;
  }
  .contact__line {
    font-family: "Inter", sans-serif;
    font-weight: 400;
    font-size: 14px;
  }
  .contact__phone { top: 161px; word-spacing: 3px; }
  .contact__email { top: 181px; }
  .contact__license {
    top: 225px; left: 24px;
    font-family: "Space Mono", monospace;
    font-style: italic;
    font-weight: 700;
    font-size: 16px;
    letter-spacing: 1px;
  }
</style>
</head>
<body>

  <section class="card card--back" aria-label="Card back">
    <div class="block back__fade-column"></div>
    <div class="block back__fade-band"></div>
    <div class="rule rule--v" style="left:77px; top:0; height:275px;"></div>
    <div class="rule rule--v" style="left:232px; top:0; height:275px;"></div>
    <div class="rule rule--h" style="left:0; top:203px; width:155px;"></div>
    <div class="rule rule--v" style="left:154px; top:73px; height:131px;"></div>
    <div class="rule rule--h" style="left:154px; top:73px; width:326px;"></div>
    <div class="brand back__brand">
      <div class="brand__name">KESTREL</div>
      <div>ROOFING &amp;<br>RESTORATION</div>
    </div>
  </section>

  <section class="card card--front" aria-label="Card front">
    <div class="block front__top-band"></div>
    <div class="block front__corner"></div>
    <div class="rule rule--v" style="left:39px; top:0; height:73px;"></div>
    <div class="rule rule--h" style="left:0; top:73px; width:311px;"></div>
    <div class="rule rule--v" style="left:310px; top:73px; height:90px;"></div>
    <div class="rule rule--h" style="left:310px; top:162px; width:170px;"></div>
    <div class="brand front__brand">
      <div class="brand__name">KESTREL</div>
      <div class="brand__divider"></div>
      <div>ROOFING &amp;<br>RESTORATION</div>
    </div>
    <div class="contact contact__name">Dana Whitlock</div>
    <div class="contact contact__line contact__phone">012 555 0147</div>
    <div class="contact contact__line contact__email">info@kestrelroofing.com</div>
    <div class="contact contact__license">5503918274</div>
  </section>

</body>
</html>
```